business card design for luxurious real estate brand

using the attached logo, i am looking for a 2-sided business card design. the back should be the gold logo on black background. the front needs to include: gold logo, name, phone, email, and website

Industry/Entity Type

real estate

Contact Information for Business Card

logo, name, email, phone, website

Font styles to use
Sans Serif

```html
<!DOCTYPE html>
<html lang="en">
<head>
<meta charset="UTF-8">
<title>Casa Lumen – Business Card</title>
<link href="https://fonts.googleapis.com/css2?family=Montserrat:wght@400;500;700&display=swap" rel="stylesheet">
<style>
  :root {
    --backdrop: #5f6063;
    --gold: #f5c400;
    --gold-deep: #e0b200;
    --ink: #060606;
    --paper-text: #111111;
    --muted: #d9d9d9;
  }
  * { box-sizing: border-box; margin: 0; padding: 0; }
  html, body {
    width: 1200px;
    height: 900px;
    overflow: hidden;
  }
  body {
    background: var(--backdrop);
    font-family: "Montserrat", Arial, sans-serif;
    position: relative;
  }
  .card {
    position: absolute;
    width: 560px;
    height: 320px;
    border-radius: 3px;
    box-shadow: 0 14px 30px rgba(0,0,0,0.35);
  }
  .card--back {
    left: 190px;
    top: 80px;
    background: linear-gradient(90deg, var(--gold-deep), var(--gold));
    display: flex;
    align-items: center;
    justify-content: center;
  }
  .card--front {
    left: 450px;
    top: 490px;
    background: var(--ink);
  }
  .brand {
    display: flex;
    align-items: center;
    gap: 12px;
    font-weight: 500;
    letter-spacing: 0.28em;
    text-transform: uppercase;
  }
  .brand__mark {
    width: 18px;
    height: 18px;
  }
  .card--back .brand {
    color: var(--paper-text);
    font-size: 30px;
  }
  .card--back .brand__mark { background: var(--paper-text); }
  .card--front .brand {
    position: absolute;
    right: 44px;
    top: 62px;
    color: var(--gold);
    font-size: 24px;
  }
  .card--front .brand__mark { background: var(--gold); width: 15px; height: 15px; }
  .divider {
    position: absolute;
    left: 198px;
    right: 34px;
    top: 176px;
    height: 1px;
    background: var(--gold);
    opacity: 0.8;
  }
  .holder {
    position: absolute;
    left: 40px;
    top: 164px;
  }
  .holder__name {
    color: var(--gold);
    font-weight: 700;
    font-size: 17px;
    letter-spacing: 0.01em;
  }
  .holder__role {
    color: var(--muted);
    font-size: 13px;
    margin-top: 2px;
  }
  .contacts {
    position: absolute;
    left: 40px;
    top: 232px;
    list-style: none;
  }
  .contacts__item {
    display: flex;
    align-items: center;
    gap: 9px;
    color: var(--muted);
    font-size: 13px;
    line-height: 22px;
  }
  .contacts__icon {
    width: 13px;
    height: 13px;
    fill: var(--gold);
    flex: none;
  }
</style>
</head>
<body>

  <section class="card card--back" aria-label="Card back">
    <div class="brand"><span class="brand__mark"></span>Casa Lumen</div>
  </section>

  <section class="card card--front" aria-label="Card front">
    <div class="brand"><span class="brand__mark"></span>Casa Lumen</div>
    <div class="divider"></div>

    <div class="holder">
      <div class="holder__name">ALEX MORENO</div>
      <div class="holder__role">Director</div>
    </div>

    <ul class="contacts">
      <li class="contacts__item">
        <svg class="contacts__icon" viewBox="0 0 16 16" aria-hidden="true">
          <path d="M3.6 1.5l2.4 2.6-1.3 2c.9 1.9 2.3 3.3 4.2 4.2l2-1.3 2.6 2.4-1.4 2.4C7.6 13.6 2.4 8.4 1.2 3z"/>
        </svg>
        300-555-0142
      </li>
      <li class="contacts__item">
        <svg class="contacts__icon" viewBox="0 0 16 16" aria-hidden="true">
          <path d="M1 3h14v10H1z M2.5 4.5l5.5 4 5.5-4" fill="none" stroke="currentColor"/>
          <path d="M1 3h14v10H1zM2.2 4.2v.3L8 8.7l5.8-4.2v-.3z" fill-rule="evenodd"/>
        </svg>
        info@casalumen.com
      </li>
      <li class="contacts__item">
        <svg class="contacts__icon" viewBox="0 0 16 16" aria-hidden="true">
          <path d="M8 1a7 7 0 1 0 0 14A7 7 0 0 0 8 1zm0 1.4c.8 0 1.8 1.6 2.1 4.1H5.9C6.2 4 7.2 2.4 8 2.4zM2.5 7.5h2.1c0 .4 0 .7.1 1H2.5a5.6 5.6 0 0 1 0-1zm.4 2.4h2c.2 1.3.6 2.4 1.1 3.2a5.6 5.6 0 0 1-3.1-3.2zM8 13.6c-.8 0-1.7-1.4-2-3.7h4c-.3 2.3-1.2 3.7-2 3.7zm2-.5c.5-.8.9-1.9 1.1-3.2h2a5.6 5.6 0 0 1-3.1 3.2zm1.4-4.6c0-.3.1-.6.1-1h2.1a5.6 5.6 0 0 1 0 1zM11.4 6.5c-.2-1.4-.6-2.6-1.2-3.4a5.6 5.6 0 0 1 3.2 3.4z"/>
        </svg>
        www.casalumen.com
      </li>
    </ul>
  </section>

</body>
</html>
```